hi all

Im after a new age looking business card with my company logo on it

must include these details, I would like the PH and Email to be symbols

If the colours used for card could be kept within the colours used in logo that I have supplied that would be great, if another colour is to be used dark grey would be ok. no light bulbs etc thanks

Details below to be incorporated on card

Damian Holloway

Lic E871302

PH 0219647381

E info@brightvaleelectrical.example.nz

Domestic Commercial Industrial Electricians

```html
<!DOCTYPE html>
<html lang="en">
<head>
<meta charset="utf-8">
<title>Brightvale Electrical – Business Card</title>
<link rel="stylesheet" href="https://fonts.googleapis.com/css2?family=Roboto:wght@400;500;700&display=swap">
<style>
  :root {
    --stage: #3a3a3d;
    --card-dark: #222223;
    --card-light: #ffffff;
    --brand-blue: #1273c0;
    --ink: #1a1a1a;
    --muted: #2b2b2b;
  }
  * { box-sizing: border-box; margin: 0; padding: 0; }
  html, body { width: 1200px; height: 1200px; overflow: hidden; }
  body {
    background: var(--stage);
    font-family: "Roboto", Arial, sans-serif;
    display: flex;
    flex-direction: column;
    align-items: center;
    justify-content: center;
    gap: 60px;
  }
  .card {
    width: 840px;
    height: 480px;
    border-radius: 30px;
    position: relative;
    overflow: hidden;
    box-shadow: 0 14px 30px rgba(0,0,0,0.35);
  }

  /* Back side */
  .card--back {
    background: var(--card-dark);
    display: flex;
    align-items: center;
    justify-content: center;
  }
  .brand {
    display: flex;
    align-items: center;
    gap: 18px;
    color: var(--brand-blue);
    font-weight: 700;
    text-transform: uppercase;
    line-height: 1;
  }
  .brand__dot {
    border-radius: 50%;
    background: var(--brand-blue);
    flex: none;
  }
  .card--back .brand { font-size: 52px; letter-spacing: 4px; }
  .card--back .brand__dot { width: 34px; height: 34px; }

  /* Front side */
  .card--front { background: var(--card-light); }
  .front__body {
    position: absolute;
    left: 0; right: 0; top: 0;
    height: 400px;
    display: flex;
    align-items: center;
    padding: 0 50px 0 60px;
  }
  .front__brand {
    width: 330px;
    flex: none;
  }
  .card--front .brand { font-size: 30px; letter-spacing: 2px; gap: 12px; flex-wrap: wrap; }
  .card--front .brand__dot { width: 22px; height: 22px; }
  .brand__stack { display: flex; flex-direction: column; gap: 8px; }
  .divider {
    width: 2px;
    height: 190px;
    background: var(--muted);
    margin: 0 34px 0 20px;
    flex: none;
  }
  .contact { display: flex; flex-direction: column; }
  .contact__name {
    color: var(--brand-blue);
    font-weight: 700;
    font-size: 34px;
    text-transform: uppercase;
    letter-spacing: 0.5px;
  }
  .contact__licence {
    font-size: 16px;
    font-weight: 500;
    color: var(--ink);
    margin-top: 4px;
  }
  .contact__rule {
    width: 46px;
    height: 3px;
    background: var(--brand-blue);
    margin: 16px 0 20px;
  }
  .contact__line {
    display: flex;
    align-items: center;
    gap: 10px;
    font-size: 21px;
    color: var(--ink);
    margin-bottom: 8px;
  }
  .contact__line svg { width: 20px; height: 20px; flex: none; fill: var(--brand-blue); }
  .front__band {
    position: absolute;
    left: 0; right: 0; bottom: 0;
    height: 80px;
    background: var(--brand-blue);
    display: flex;
    align-items: center;
    justify-content: center;
    color: #ffffff;
    font-weight: 700;
    font-size: 22px;
    letter-spacing: 1px;
    text-transform: uppercase;
  }
</style>
</head>
<body>

  <section class="card card--back" aria-label="Card back">
    <div class="brand">
      <span class="brand__dot"></span>
      <span>Brightvale Electrical</span>
    </div>
  </section>

  <section class="card card--front" aria-label="Card front">
    <div class="front__body">
      <div class="front__brand">
        <div class="brand">
          <span class="brand__dot"></span>
          <span class="brand__stack"><span>Brightvale</span><span>Electrical</span></span>
        </div>
      </div>
      <div class="divider"></div>
      <div class="contact">
        <div class="contact__name">Damian Holloway</div>
        <div class="contact__licence">LIC E871302</div>
        <div class="contact__rule"></div>
        <div class="contact__line">
          <svg viewBox="0 0 24 24" aria-hidden="true"><path d="M6.6 10.8a15.1 15.1 0 0 0 6.6 6.6l2.2-2.2a1 1 0 0 1 1-.25 11.4 11.4 0 0 0 3.6.57 1 1 0 0 1 1 1V20a1 1 0 0 1-1 1A17 17 0 0 1 3 4a1 1 0 0 1 1-1h3.5a1 1 0 0 1 1 1c0 1.25.2 2.45.57 3.6a1 1 0 0 1-.25 1z"/></svg>
          <span>0219647381</span>
        </div>
        <div class="contact__line">
          <svg viewBox="0 0 24 24" aria-hidden="true"><path d="M3 5h18a1 1 0 0 1 1 1v12a1 1 0 0 1-1 1H3a1 1 0 0 1-1-1V6a1 1 0 0 1 1-1zm9 7.2L4.2 7H4v.4l8 5.3 8-5.3V7h-.2z"/></svg>
          <span>info@brightvaleelectrical.example.nz</span>
        </div>
      </div>
    </div>
    <div class="front__band">Domestic Commercial Industrial Electricians</div>
  </section>

</body>
</html>
```